Business Card Design

We need a business card for a new furniture company in Utah. We are introducing a fresh new concept in Utah and would like a card to reflect to buyers that they can buy quality furniture and get it NOW. I am open to just about any color scheme, but I would like something that pops.

Industry/Entity Type

Business

Contact Information for Business Card

Sofa Haven, Glen Marsh
41 S. Pine Hollow Lane
Cedar Brook Utah 84217

```html
<!DOCTYPE html>
<html lang="en">
<head>
<meta charset="utf-8">
<title>Sofa Haven – Business Card</title>
<link rel="stylesheet" href="https://fonts.googleapis.com/css2?family=Orbitron:wght@600;800&display=swap">
<style>
  :root {
    --card-amber: #c98c3c;
    --panel-rust: #b5651f;
    --ink: #0c0b09;
  }
  html, body {
    margin: 0;
    padding: 0;
    overflow: hidden;
    background: #ffffff;
  }
  .business-card {
    position: relative;
    width: 1200px;
    height: 686px;
    overflow: hidden;
    background: radial-gradient(circle at 40% 40%, #cf9443 0%, var(--card-amber) 70%);
    font-family: "Orbitron", sans-serif;
    color: var(--ink);
    text-transform: uppercase;
  }
  .corner-panel {
    position: absolute;
    inset: 0;
    width: 1200px;
    height: 686px;
  }
  .corner-panel polygon {
    fill: var(--panel-rust);
  }
  .company-name {
    position: absolute;
    left: 43px;
    top: 176px;
    margin: 0;
    font-size: 64px;
    font-weight: 800;
    letter-spacing: 2px;
    line-height: 1;
  }
  .contact-block {
    position: absolute;
    right: 68px;
    text-align: right;
    font-weight: 800;
    margin: 0;
  }
  .person-name {
    top: 294px;
    right: 71px;
    font-size: 27px;
    letter-spacing: 1.5px;
    line-height: 1;
  }
  .street-address {
    top: 496px;
    font-size: 29px;
    letter-spacing: 1.5px;
    line-height: 44px;
    font-style: normal;
  }
</style>
</head>
<body>
  <main class="business-card">
    <svg class="corner-panel" viewBox="0 0 1200 686" aria-hidden="true">
      <polygon points="1200,0 539,459 609,686 1200,686"/>
    </svg>

    <h1 class="company-name">Sofa Haven</h1>

    <p class="contact-block person-name">Glen Marsh</p>

    <address class="contact-block street-address">
      41 S. Pine Hollow Lane<br>
      Cedar Brook<br>
      Utah 84217
    </address>
  </main>
</body>
</html>
```